Outstanding but small benefit administration firm serving large clients needs a website redesign

While the content on our current website is fine, when people arrive at our website, they know immediately that it was designed years ago. We are looking for something that can potentially be maintained on a content management system because we would like to hire a google certified expert to help with adwords and they often want to change the website or add meta data. We want the design to be mobile device friendly.

As for our company, we stress data accuracy, client customization and outstanding customer service. All of our competitors are large corporations (Corvellan, Tolbin, Qualix, PerkWaypoint, etc.). When we get a client, they stay with us. So many of our competitors do a horrible job with administration that many companies just think that's the way it is in this industry. We need to change that thinking! There is someone who can do it right at a reasonable price. We have very few out of scope fees. RMT knows how to make the transition from one administrator to us as painless as possible.

We like our current colors. We don't have a lot of time to write additional content.

Target Market(s)

Companies with 5,000 to 50,000 employees

Coding

Coded - Design and coding required

Number of Pages Required

2 page

Font styles to use
Sans Serif

Requirements
Must have
• If everything doesn't fit on one page, please show me what the second page would look like. For example, if there are See More links, what happens?
• We need for people to be able to submit short contact us with their company name as a required field.
• Ideally this website will be put on wordpress or something similar.
• Must be mobile device friendly.
Should not have
• Login, Register, Maps of our location, website search

```html
<!DOCTYPE html>
<html lang="en">
<head>
<meta charset="utf-8">
<title>Rivermark Management Trust</title>
<link href="https://fonts.googleapis.com/css2?family=Montserrat:wght@400;500;600;700&display=swap" rel="stylesheet">
<style>
:root{
  --blue:#4fb8e8;
  --green:#7cc142;
  --lime:#c0d631;
  --ink:#555a5f;
  --muted:#6d7378;
  --white:#ffffff;
  --rule:#dcdcdc;
  --icon:#7a7f84;
}
*{box-sizing:border-box;margin:0;padding:0}
html,body{width:1162px;height:1200px;overflow:hidden;background:var(--white)}
body{font-family:'Montserrat',sans-serif;color:var(--ink);position:relative}

.site-header{position:absolute;top:0;left:0;width:1162px;height:46px;z-index:3}
.brand{position:absolute;left:228px;top:14px;display:flex;align-items:center;gap:6px;font-size:10.5px;font-weight:500;color:var(--ink)}
.brand-dot{width:11px;height:11px;border-radius:50%;background:var(--blue)}
.main-nav{position:absolute;top:19px;left:535px;display:flex;font-size:7.6px;font-weight:500;letter-spacing:.3px}
.main-nav a{color:var(--ink);text-decoration:none;margin-right:33px;display:flex;align-items:center;gap:4px}
.main-nav a:last-child{margin-right:0}
.caret{width:0;height:0;border-left:2.5px solid transparent;border-right:2.5px solid transparent;border-top:3px solid var(--ink)}

.hero{position:absolute;top:0;left:0;width:1162px;height:593px;overflow:hidden}
.hero-photo{position:absolute;inset:0;background:linear-gradient(180deg,#eef5fa 0%,#e9eef2 45%,#dfe3e6 70%,#eceef0 100%)}
.hero-content{position:absolute;top:164px;left:0;width:1162px;text-align:center}
.hero-mark{display:flex;flex-direction:column;align-items:center;gap:10px;margin-bottom:72px}
.hero-mark .dot{width:26px;height:26px;border-radius:50%;background:var(--blue)}
.hero-mark .name{font-size:22px;font-weight:600;color:var(--green);letter-spacing:1px}
.eyebrow{font-size:10px;line-height:12px;color:var(--blue);letter-spacing:.6px;font-weight:500}
.hero-title{font-size:17.5px;line-height:22px;font-weight:700;color:#4d5257;letter-spacing:.6px;margin-top:1px}
.hero-lede{width:440px;margin:3px auto 0;font-size:8.8px;line-height:12.8px;color:var(--muted)}
.btn-contact{display:inline-block;margin-top:16px;width:176px;height:30px;line-height:30px;border-radius:15px;background:var(--blue);color:var(--white);font-size:10.5px;font-weight:600;letter-spacing:.8px;text-decoration:none}
.scroll-tab{position:absolute;left:567px;top:563px;width:28px;height:30px;background:var(--white);border-radius:14px 14px 0 0;display:flex;align-items:center;justify-content:center}

.services{position:absolute;top:628px;left:227px;display:flex;gap:36px}
.service-card{width:212px;height:42px;display:flex;color:var(--white)}
.service-card .label{flex:1;padding:8px 0 0 18px;font-size:10px;font-weight:500;line-height:13px;letter-spacing:.3px}
.service-card .toggle{width:45px;border-left:1px solid rgba(255,255,255,.45);display:flex;align-items:center;justify-content:center}
.card-blue{background:var(--blue)}
.card-green{background:var(--green)}
.card-lime{background:var(--lime)}

.testimonials{position:absolute;top:709px;left:0;width:1162px;height:293px;border-bottom:2px solid var(--green);text-align:center;color:var(--white)}
.testimonials-photo{position:absolute;inset:0;background:radial-gradient(ellipse at 50% 40%,#6d6a67 0%,#55555a 55%,#3f4247 100%)}
.testimonials-inner{position:relative;padding-top:100px}
.testimonials h2{font-size:17.5px;font-weight:700;letter-spacing:.5px;display:flex;justify-content:center;align-items:flex-start;gap:5px}
.testimonials h2 .quote-mark{color:var(--green);font-size:18px;line-height:12px}
.testimonials blockquote{width:420px;margin:14px auto 0;font-size:8.8px;line-height:12.8px}
.testimonials cite{display:block;margin-top:13px;font-style:normal;font-weight:700;font-size:8.4px}

.site-footer{position:absolute;top:1003px;left:0;width:1162px;text-align:center}
.footer-mark{margin-top:27px;display:flex;flex-direction:column;align-items:center;gap:4px}
.footer-mark .dot{width:8px;height:8px;border-radius:50%;background:var(--blue)}
.footer-mark .name{font-size:10px;line-height:12px;font-weight:600;color:var(--green)}
.copyright{margin-top:24px;font-size:7px;letter-spacing:.4px;color:var(--muted)}
.social{margin-top:16px;display:flex;justify-content:center;gap:13px}
.social span{width:8px;height:8px;border-radius:50%;background:var(--icon)}
.footer-links{width:286px;margin:17px auto 0;border-top:1px solid var(--rule);padding-top:16px;display:flex;justify-content:space-between;font-size:7px;letter-spacing:.4px}
.footer-links a{color:var(--muted);text-decoration:none}
</style>
</head>
<body>

<section class="hero">
  <div class="hero-photo" role="img" aria-label="Bright office meeting room with business people seated around a white table"></div>
  <div class="hero-content">
    <div class="hero-mark"><span class="dot"></span><span class="name">RMT</span></div>
    <p class="eyebrow">A BOUTIQUE ORGANIZATION</p>
    <h1 class="hero-title">PROVIDING LARGE PLAN SPONSORS</h1>
    <p class="hero-lede">with a customer service model using only trained benefit professionals and a totally cutomizable, highly flexible technology platform. This unique model allows RMT to provide large company IT capabilities, unparalleled service and very competitive fees.</p>
    <a class="btn-contact" href="#">CONTACT US</a>
  </div>
  <div class="scroll-tab">
    <svg width="12" height="14" viewBox="0 0 12 14"><path d="M6 1v11M1.5 7.5L6 12l4.5-4.5" fill="none" stroke="#7cc142" stroke-width="1.4"/></svg>
  </div>
</section>

<header class="site-header">
  <div class="brand"><span class="brand-dot"></span>Rivermark Management Trust</div>
  <nav class="main-nav">
    <a href="#">WHY RMT <span class="caret"></span></a>
    <a href="#">SERVICES <span class="caret"></span></a>
    <a href="#">TECHNOLOGY</a>
    <a href="#">CASE STUDIES</a>
    <a href="#">CONTACT US</a>
  </nav>
</header>

<section class="services">
  <div class="service-card card-blue"><div class="label">HEALTH AND WELFARE<br>ADMINISTRATION</div><div class="toggle"><svg width="14" height="14"><path d="M7 0v14M0 7h14" stroke="#fff" stroke-width="1.6"/></svg></div></div>
  <div class="service-card card-green"><div class="label">DEFINED BENEFIT<br>ADMINISTRATION</div><div class="toggle"><svg width="14" height="14"><path d="M7 0v14M0 7h14" stroke="#fff" stroke-width="1.6"/></svg></div></div>
  <div class="service-card card-lime"><div class="label">BENEFIT CONSULTING<br>SERVICES</div><div class="toggle"><svg width="14" height="14"><path d="M7 0v14M0 7h14" stroke="#fff" stroke-width="1.6"/></svg></div></div>
</section>

<section class="testimonials">
  <div class="testimonials-photo" role="img" aria-label="Soft-focus group of smiling business colleagues"></div>
  <div class="testimonials-inner">
    <h2><span class="quote-mark">&ldquo;</span>TESTIMONIALS</h2>
    <blockquote>&ldquo;RMT has been our vendor from their inception. They handle our most complex plans with a seemingly infinite amount of patience and professionalism. We get glowing reports from our location HR managers, participants and vendors on their performance.&rdquo;</blockquote>
    <cite>Daniel Osterlund - Vice President, Compensation and Benefits</cite>
  </div>
</section>

<footer class="site-footer">
  <div class="footer-mark"><span class="dot"></span><span class="name">RMT</span></div>
  <p class="copyright">&copy; 2016 RIVERMARK MANAGEMENT TRUST, INC. ALL RIGHTS RESERVED</p>
  <div class="social"><span aria-label="Social link"></span><span aria-label="Social link"></span><span aria-label="Social link"></span></div>
  <nav class="footer-links">
    <a href="#">CONTACT US</a>
    <a href="#">DISCLAIMER &amp; TERMS OF USE</a>
    <a href="#">PRIVACY POLICY</a>
  </nav>
</footer>

</body>
</html>
```